Website Design for a Project Management Consulting Business

I have a logo design already and now I need a website.
I am a project manager and run my own consulting business.
Currently I am under contract with 3 major Keystone 300 companies. I'd like a website I can direct current and future clients.
My job is running IT projects and working with developers to deliver business priorities.
The website should be professional and clean - I work IT projects and would like to incorporate that into any theme.
I'd like the site to have several page or breakoff links - sections would include : about me, about my services, a page to display all of my certification badges, another page to talk about highlights from past projects and so on.
Looking for a collaborative experience.
Updates

Slow in providing feedback

Industry/Entity Type

Keystone 300 Consulting Firm - Project Management

Coding

Coded - Design and coding required

Number of Pages Required

1 page

Font styles to use
Serif

Colors
0094D4
00A9DD
6FCCEA
C7EBF8
E9F6FB
EE7325
F08F49
F5BC92
FAE3D3
FDF4ED

Requirements
Must have
• Sections that are a must: About Me (bio), About My Services, About my Certifications and Credentials, Experience on Past Projects,
Nice to have
• I have added the logo below - I'd like to use the logo and have it prominent ; should be professional and inviting

```html
<!DOCTYPE html>
<html lang="en">
<head>
<meta charset="utf-8">
<title>Meridian Project Advisory — Consulting</title>
<link rel="stylesheet" href="https://fonts.googleapis.com/css2?family=Barlow:wght@400;500;600;700;800&family=Open+Sans:wght@400;600&display=swap">
<style>
:root{
  --blue:#0094D4;
  --blue-bright:#00A9DD;
  --blue-soft:#6FCCEA;
  --blue-pale:#C7EBF8;
  --blue-mist:#E9F6FB;
  --orange:#EE7325;
  --orange-soft:#F08F49;
  --orange-pale:#F5BC92;
  --navy:#1B2A4A;
  --ink:#333b48;
  --grey:#6d7480;
  --line:#d9dde3;
  --foot:#f3f4f6;
  --white:#ffffff;
}
*{box-sizing:border-box;margin:0;padding:0}
html,body{width:1200px;height:3744px;overflow:hidden;background:var(--white)}
body{position:relative;font-family:"Open Sans",Arial,sans-serif;color:var(--ink)}
.abs{position:absolute}
.h-font{font-family:"Barlow",Arial,sans-serif}
.brand{display:flex;align-items:center;gap:12px}
.brand-mark{width:40px;height:40px;background:var(--blue)}
.brand-name{font-family:"Barlow",Arial,sans-serif;font-weight:700;font-size:22px;line-height:1.05;color:var(--navy);letter-spacing:.5px;text-transform:uppercase}
.top-contact{display:flex;align-items:center;gap:10px;font-size:14px}
.top-contact small{display:block;color:var(--grey);font-size:13px}
.top-contact b{color:var(--navy);font-weight:600}
.nav{left:140px;top:88px;width:920px;height:32px;background:var(--blue-bright);display:flex;align-items:center;padding-left:24px;gap:22px}
.nav a{color:var(--white);font-family:"Barlow",Arial,sans-serif;font-weight:600;font-size:13px;text-decoration:none;letter-spacing:.5px}
.nav span{color:var(--white);opacity:.7;font-size:12px}
.photo{background:linear-gradient(160deg,#5a5f66,#2c2f35)}
.hero-title{font-family:"Barlow",Arial,sans-serif;font-weight:800;text-transform:uppercase;line-height:1;white-space:nowrap}
.rule{height:3px;width:60px;background:var(--orange)}
.btn{display:inline-block;background:var(--orange);color:var(--white);font-family:"Barlow",Arial,sans-serif;font-weight:700;font-size:14px;letter-spacing:.5px;padding:11px 26px;border-radius:22px;text-transform:uppercase}
.section-title{width:1200px;left:0;text-align:center;font-family:"Barlow",Arial,sans-serif;font-weight:800;font-size:46px;color:var(--navy);text-transform:uppercase}
.section-title em{font-style:normal;color:var(--blue)}
.section-rule{left:570px;width:60px;height:3px;background:var(--orange)}
.services{left:160px;top:740px;width:880px;height:240px;display:grid;grid-template-columns:repeat(3,1fr);grid-template-rows:repeat(2,1fr)}
.service{display:flex;align-items:center;justify-content:center;text-align:center;font-family:"Barlow",Arial,sans-serif;font-weight:700;font-size:17px;color:var(--navy);line-height:1.3;border-color:var(--blue-soft);border-style:solid;border-width:0}
.service:nth-child(-n+3){border-bottom-width:2px}
.service:not(:nth-child(3n)){border-right-width:2px}
.body-text{font-size:15px;line-height:1.65;color:var(--grey)}
.stat b{display:block;font-family:"Barlow",Arial,sans-serif;font-size:34px;font-weight:800;color:var(--orange)}
.stat span{font-size:14px;font-weight:600;color:var(--navy)}
.badges{left:160px;top:1830px;width:880px;height:120px;display:flex;align-items:center;justify-content:space-between}
.badge-row{display:flex;gap:38px;align-items:center}
.badge{width:86px;height:86px;border-radius:50%;background:var(--blue-mist);border:2px solid var(--blue-pale)}
.card-label{font-family:"Barlow",Arial,sans-serif;font-weight:700;font-size:19px;color:var(--navy);text-align:center;text-transform:uppercase;line-height:1.25;width:260px}
.contact-left{left:0;top:3060px;width:520px;height:410px;background:var(--orange)}
.contact-right{left:520px;top:3060px;width:680px;height:410px;background:var(--blue-bright)}
.contact-row{display:flex;align-items:center;gap:12px;color:var(--white);font-size:14px;white-space:nowrap}
.contact-row .ic{width:28px;height:28px;border-radius:50%;background:var(--white);display:flex;align-items:center;justify-content:center;flex:none}
.field{position:absolute;border:1.5px solid var(--white);border-radius:4px;height:34px;color:var(--white);font-size:12px;font-weight:600;padding:9px 12px;letter-spacing:.5px}
.footer{left:0;top:3470px;width:1200px;height:274px;background:var(--foot)}
.foot-title{font-family:"Barlow",Arial,sans-serif;font-weight:800;font-size:18px;color:var(--navy);text-transform:uppercase}
.foot-list{list-style:none;font-size:13px;color:var(--grey);line-height:1.9}
.foot-list li::before{content:"• ";color:var(--blue)}
.social{display:flex;gap:14px}
.social i{display:block;width:14px;height:14px;border-radius:50%;background:var(--navy)}
</style>
</head>
<body>

<header>
  <div class="abs brand" style="left:160px;top:24px">
    <div class="brand-mark"></div>
    <div class="brand-name">Meridian Project<br>Advisory</div>
  </div>
  <div class="abs top-contact" style="left:650px;top:24px">
    <svg width="18" height="18" viewBox="0 0 24 24"><path d="M6.6 10.8a15 15 0 0 0 6.6 6.6l2.2-2.2c.3-.3.7-.4 1-.2 1.1.4 2.300.6 3.6.6.6 0 1 .4 1 1V20c0 .6-.4 1-1 1A17 17 0 0 1 3 4c0-.6.4-1 1-1h3.5c.6 0 1 .4 1 1 0 1.3.2 2.5.6 3.6.1.3 0 .7-.2 1z" fill="var(--orange)"/></svg>
    <div><small>Call Me</small><b>(555) 014-2290</b></div>
  </div>
  <div class="abs top-contact" style="left:820px;top:24px">
    <svg width="18" height="18" viewBox="0 0 24 24"><rect x="2" y="5" width="20" height="14" rx="2" fill="none" stroke="var(--orange)" stroke-width="2"/><path d="M3 6l9 7 9-7" fill="none" stroke="var(--orange)" stroke-width="2"/></svg>
    <div><small>Email Me</small><b>hello@meridianadvisory.com</b></div>
  </div>
  <nav class="abs nav">
    <a>ABOUT ME</a><span>|</span><a>MY SERVICES</a><span>|</span><a>CERTIFICATIONS AND CREDENTIALS</a><span>|</span><a>EXPERIENCE</a><span>|</span><a>CONTACT</a>
  </nav>
</header>

<section>
  <div class="abs photo" style="left:160px;top:144px;width:420px;height:428px" role="img" aria-label="Portrait photo of the consultant in a suit"></div>
  <div class="abs" style="left:630px;top:244px;width:410px">
    <div class="hero-title" style="font-size:34px;color:var(--navy)">Extensive Experienced</div>
    <div class="hero-title" style="font-size:54px;color:var(--blue);margin-top:6px">Consultant</div>
    <div class="rule" style="margin-top:14px"></div>
    <p class="body-text" style="margin-top:14px;font-size:16px">Serves as Principal Lead Consultant on waterfall and agile contract opportunities.</p>
    <div style="margin-top:20px"><span class="btn">My Experience</span></div>
  </div>
  <div class="abs" style="left:160px;top:600px;width:880px;height:1px;background:var(--line)"></div>
</section>

<section>
  <h2 class="abs section-title" style="top:650px">About <em>My Services</em></h2>
  <div class="abs section-rule" style="top:712px"></div>
  <div class="abs services">
    <div class="service">LEADING SAFE AGILE<br>SCRUM TEAMS</div>
    <div class="service">LEADING SAFE AGILE<br>SCRUM TEAMS</div>
    <div class="service">LEADING SAFE AGILE<br>SCRUM TEAMS</div>
    <div class="service">LEADING SAFE AGILE<br>SCRUM TEAMS</div>
    <div class="service">LEADING SAFE AGILE<br>SCRUM TEAMS</div>
    <div class="service">LEADING SAFE AGILE<br>SCRUM TEAMS</div>
  </div>
</section>

<section>
  <div class="abs" style="left:0;top:1040px;width:1200px;height:640px;background:linear-gradient(180deg,var(--white),var(--blue-mist))"></div>
  <div class="abs" style="left:160px;top:1120px;width:420px">
    <h2 class="h-font" style="font-size:46px;font-weight:800;color:var(--navy);text-transform:uppercase">About <span style="color:var(--blue)">Me</span></h2>
    <div class="rule" style="margin-top:8px"></div>
    <p class="body-text" style="margin-top:24px">Daniel Whitford is the Owner of Meridian Project Advisory, LLC and serves as Principal Lead Consultant on waterfall and agile contract opportunities.</p>
    <p class="body-text" style="margin-top:18px">Meridian Project Advisory, LLC has engaged on a contract basis with Keystone 300 companies across various industries including banking and credit unions, global supply chain, and international food distribution. Daniel Whitford brings 12 years of experience ...</p>
    <div style="display:flex;gap:60px;margin-top:24px">
      <div class="stat"><b>500+</b><span>Satisfied Clients</span></div>
      <div class="stat"><b>99%</b><span>Success of Works</span></div>
    </div>
    <div style="margin-top:26px"><span class="btn">Know More</span></div>
  </div>
  <div class="abs" style="left:600px;top:1140px;width:440px;height:540px;background:linear-gradient(180deg,#8aa0b8,#3f5570);border-radius:220px 220px 0 0" role="img" aria-label="Standing photo of the consultant in a checked blazer"></div>
</section>

<section>
  <h2 class="abs section-title" style="top:1740px">Certifications <em>&amp; Credentials</em></h2>
  <div class="abs section-rule" style="top:1802px"></div>
  <div class="abs badges">
    <svg width="24" height="40" viewBox="0 0 24 40"><path d="M20 4L4 20l16 16" fill="none" stroke="var(--orange)" stroke-width="4"/></svg>
    <div class="badge-row">
      <div class="badge" role="img" aria-label="Certification badge"></div>
      <div class="badge" role="img" aria-label="Certification badge"></div>
      <div class="badge" role="img" aria-label="Certification badge"></div>
      <div class="badge" role="img" aria-label="Certification badge"></div>
      <div class="badge" role="img" aria-label="Certification badge"></div>
      <div class="badge" role="img" aria-label="Certification badge"></div>
    </div>
    <svg width="24" height="40" viewBox="0 0 24 40"><path d="M4 4l16 16L4 36" fill="none" stroke="var(--orange)" stroke-width="4"/></svg>
  </div>
</section>

<section>
  <div class="abs photo" style="left:160px;top:2060px;width:420px;height:380px;background:linear-gradient(160deg,#6f7a88,#36404c)" role="img" aria-label="Photo of the consultant in an office"></div>
  <div class="abs" style="left:630px;top:2090px;width:410px">
    <div class="hero-title" style="font-size:40px;color:var(--navy)">Trusted by Biggest</div>
    <div class="hero-title" style="font-size:40px;color:var(--blue);margin-top:4px">Business Names</div>
    <div class="rule" style="margin-top:14px"></div>
    <p class="body-text" style="margin-top:18px">Lorem ipsum dolor sit amet, consectetur adipiscing elit, sed do eiusmod tempor incididunt ut labore et dolore magna aliqua. Ut enim ad minim veniam, quis nostrud exercitation ullamco laboris nisi ut aliquip ex ea commodo consequat.</p>
    <p class="h-font" style="margin-top:18px;font-weight:700;font-size:16px;color:var(--navy)">MARCUS ELLERY</p>
    <p style="font-size:14px;color:var(--grey)">Northgate Labs</p>
  </div>
  <div class="abs h-font" style="left:985px;top:2370px;font-size:110px;font-weight:800;color:var(--blue-pale);line-height:1">”</div>
</section>

<section>
  <h2 class="abs section-title" style="top:2580px;color:var(--blue)">Experience</h2>
  <div class="abs section-rule" style="top:2642px"></div>
  <div class="abs photo" style="left:160px;top:2700px;width:260px;height:200px" role="img" aria-label="Portrait of the consultant"></div>
  <div class="abs photo" style="left:470px;top:2700px;width:260px;height:200px;background:linear-gradient(160deg,#9aa7b6,#4c5a6a)" role="img" aria-label="Portrait of the consultant in a blazer"></div>
  <div class="abs photo" style="left:780px;top:2700px;width:260px;height:200px" role="img" aria-label="Portrait of the consultant"></div>
  <div class="abs card-label" style="left:160px;top:2930px">Senior Safe Scrum<br>Master</div>
  <div class="abs card-label" style="left:470px;top:2930px">Senior Project<br>Manger</div>
  <div class="abs card-label" style="left:780px;top:2930px">Senior Program<br>Manger</div>
</section>

<section>
  <div class="abs contact-left"></div>
  <div class="abs contact-right"></div>
  <div class="abs" style="left:160px;top:3100px;width:340px">
    <h2 class="h-font" style="font-size:44px;font-weight:800;color:var(--white);text-transform:uppercase">Get in Touch</h2>
    <div class="rule" style="background:var(--white);margin-top:8px"></div>
    <p style="margin-top:20px;font-size:14px;line-height:1.6;color:var(--white)">We'd glad to discuss your organization's situation. So please contact us via the details below, or enter your request.</p>
    <div style="margin-top:24px;display:flex;flex-direction:column;gap:14px">
      <div class="contact-row"><span class="ic"><svg width="14" height="14" viewBox="0 0 24 24"><path d="M12 2a7 7 0 0 0-7 7c0 5 7 13 7 13s7-8 7-13a7 7 0 0 0-7-7zm0 9.5A2.5 2.5 0 1 1 12 6.5a2.5 2.5 0 0 1 0 5z" fill="var(--orange)"/></svg></span><span>Address — 48 Harbor Lane,<br>Denver, CO 80202, USA</span></div>
      <div class="contact-row"><span class="ic"><svg width="14" height="14" viewBox="0 0 24 24"><path d="M6.6 10.8a15 15 0 0 0 6.6 6.6l2.2-2.2c.3-.3.7-.4 1-.2 1.1.4 2.3.6 3.6.6.6 0 1 .4 1 1V20c0 .6-.4 1-1 1A17 17 0 0 1 3 4c0-.6.4-1 1-1h3.5c.6 0 1 .4 1 1 0 1.3.2 2.5.6 3.6.1.3 0 .7-.2 1z" fill="var(--orange)"/></svg></span><span>Call Me — <b>(555) 014-2290</b></span></div>
      <div class="contact-row"><span class="ic"><svg width="14" height="14" viewBox="0 0 24 24"><rect x="2" y="5" width="20" height="14" rx="2" fill="var(--orange)"/><path d="M3 6l9 7 9-7" fill="none" stroke="var(--white)" stroke-width="2"/></svg></span><span>Email Me — <b>hello@meridianadvisory.com</b></span></div>
    </div>
  </div>
  <form>
    <div class="field" style="left:560px;top:3104px;width:230px">FIRST NAME</div>
    <div class="field" style="left:810px;top:3104px;width:230px">LAST NAME</div>
    <div class="field" style="left:560px;top:3154px;width:230px">EMAIL ADDRESS</div>
    <div class="field" style="left:810px;top:3154px;width:230px">PHONE</div>
    <div class="field" style="left:560px;top:3204px;width:230px">WEBSITE</div>
    <div class="field" style="left:810px;top:3204px;width:230px">SERVICES</div>
    <div class="field" style="left:560px;top:3254px;width:480px;height:100px">MESSAGE</div>
    <span class="abs btn" style="left:870px;top:3376px">Send Request</span>
  </form>
</section>

<footer class="abs footer">
  <div class="abs" style="left:160px;top:44px">
    <div class="foot-title">Usefull Links</div>
    <div class="rule" style="width:40px;margin-top:6px"></div>
  </div>
  <ul class="abs foot-list" style="left:160px;top:86px;width:110px">
    <li>About Me</li><li>Experience</li><li>Certifications and Credentials</li><li>Contact Us</li>
  </ul>
  <ul class="abs foot-list" style="left:290px;top:86px">
    <li>Privacy Policy</li><li>Terms &amp; Conditions</li>
  </ul>
  <div class="abs" style="left:480px;top:44px">
    <div class="foot-title">Services</div>
    <div class="rule" style="width:40px;margin-top:6px"></div>
  </div>
  <ul class="abs foot-list" style="left:480px;top:86px">
    <li>Service1</li><li>Service2</li><li>Service3</li><li>Service4</li>
  </ul>
  <div class="abs" style="left:730px;top:48px;width:310px;display:flex;flex-direction:column;align-items:center;gap:16px">
    <div class="brand"><div class="brand-mark"></div><div class="brand-name">Meridian Project<br>Advisory</div></div>
    <div class="social"><i></i><i></i><i></i><i></i></div>
    <p style="font-size:12px;color:var(--grey)">Copyright © 2022 Meridian LLC. All rights reserved.</p>
  </div>
</footer>

</body>
</html>
```